New Professional Business Web Site

We need a web design for an existing company based in Dallas called "FoxTrail".
We provide software and professional services to enterprise customers in the contact centre space. We have a global customer base but primarily US and UK.
Our initial products are as follows-
LineSight - an application that helps Vortiva contact centre managers and administrators observe individual calls in queue.
MassLoad - an application that allows Vortiva administrators to load large groups of extensions and associate them to places.
Clustra - an application that helps Vortiva customers manage multilayers of agent and place groups into hiearchical and geographical groups of groups.
We would like to see designs that use the colors black, gray, and red as this matches with our new logo we have had designed from this web site and will have available in a few days.
The final design should communicate professionalism, innovation, software, large corporation, and telecommunications.
We're looking to provide features like-
1) Interactive Support Portal for customers
2) Product Descriptions
3) Product Purchasing
4) Interactive Forum
Target Market(s)
enterprise companies interested in call center related products and services
Industry/Entity Type
Business

```html
<!DOCTYPE html>
<html lang="en">
<head>
<meta charset="utf-8">
<title>FoxTrail – Contact Centre Software</title>
<link href="https://fonts.googleapis.com/css2?family=Arimo:wght@400;700&display=swap" rel="stylesheet">
<style>
:root{
  --red:#e3141b;
  --red-dark:#a80d12;
  --black:#0b0b0b;
  --panel:#151515;
  --gray:#8a8a8a;
  --light:#d8d8d8;
  --white:#ffffff;
}
*{margin:0;padding:0;box-sizing:border-box}
html,body{width:878px;height:1200px;overflow:hidden;background:var(--black);font-family:"Arimo",Arial,sans-serif;color:var(--light)}
.page{position:relative;width:878px;height:1200px;overflow:hidden}
.header{position:absolute;left:0;top:0;width:878px;height:88px;background:linear-gradient(#fff,#e9e9e9)}
.user-links{position:absolute;right:24px;top:10px;font-size:11px;color:#555;display:flex;gap:12px}
.brand{position:absolute;left:30px;top:28px;display:flex;align-items:center;gap:8px}
.brand-mark{width:22px;height:22px;background:var(--red)}
.brand-name{font-size:34px;font-weight:700;color:#2a2a2a}
.nav{position:absolute;left:380px;top:42px;width:498px;height:36px;background:var(--red);display:flex}
.nav a{color:#fff;text-decoration:none;font-size:12px;font-weight:700;padding:0 18px;line-height:36px}
.nav a.active{background:var(--black)}
.hero{position:absolute;left:0;top:88px;width:878px;height:322px;background:radial-gradient(ellipse at 65% 40%,#c9c3bd 0%,#8f8882 35%,#4a4644 70%,#2a2828 100%)}
.hero-title{position:absolute;left:70px;top:130px;font-size:40px;font-weight:700;color:var(--white)}
.hero-sub{position:absolute;left:150px;top:188px;font-size:50px;font-weight:700;color:var(--red)}
.products{position:absolute;left:0;top:410px;width:878px;height:78px;background:linear-gradient(#2b2b2b,#111);display:flex}
.product{flex:1;padding:4px 14px}
.product-tab{display:inline-flex;align-items:center;gap:6px;background:var(--red);color:#fff;font-size:13px;font-weight:700;padding:4px 14px 4px 6px}
.product p{font-size:11px;color:#eee;margin-top:8px;display:flex;gap:8px;align-items:flex-start}
.main{position:absolute;left:0;top:488px;width:878px;height:577px}
.content{position:absolute;left:22px;top:30px;width:575px}
h2{color:var(--red);font-size:16px;font-weight:700;padding-bottom:6px;border-bottom:1px solid #3a3a3a}
.intro{font-size:10.5px;line-height:15px;color:#ccc;margin:10px 0 18px}
.intro .lead{color:var(--red);display:block;margin-bottom:4px}
.feature{display:flex;gap:16px;margin-top:16px}
.feature-photo{width:160px;height:105px;background:linear-gradient(135deg,#6e6a66,#2e2c2b);flex:none}
.feature h3{color:#fff;font-size:14px;margin-bottom:4px}
.feature .tag{color:var(--red);font-size:10px}
.feature p{font-size:10.5px;line-height:14px;width:180px;margin:4px 0 6px}
.more{display:inline-flex;align-items:center;gap:5px;font-size:10px;color:#fff}
.more i{width:12px;height:12px;background:var(--red);display:inline-block}
.sidebar{position:absolute;left:618px;top:40px;width:245px}
.services{background:linear-gradient(var(--red-dark),#5a0507);border:1px solid #c21117;padding:10px 0 12px}
.services h4,.stats h4{color:#ff8a8a;font-size:14px;font-weight:400;padding:0 14px 8px}
.services li{list-style:none;font-size:10.5px;color:#fff;padding:6px 14px 6px 40px;border-top:1px solid rgba(255,255,255,.15)}
.stats{margin-top:14px;background:#181818;border:1px solid #333;padding:10px 0;height:200px;position:relative}
.stats blockquote{margin:8px 30px;font-size:13px;line-height:17px;color:#eee}
.stats cite{display:block;text-align:right;margin-right:30px;font-size:10px;color:#aaa;font-style:normal}
.arrow{position:absolute;top:90px;width:0;height:0;border-top:8px solid transparent;border-bottom:8px solid transparent}
.arrow.left{left:8px;border-right:10px solid var(--red)}
.arrow.right{right:8px;border-left:10px solid var(--red)}
.footer{position:absolute;left:0;top:1065px;width:878px;height:115px;background:linear-gradient(#222,#0d0d0d);display:flex;padding:14px 22px 0;gap:24px}
.footer h5{color:var(--red);font-size:14px;font-weight:400;margin-bottom:8px}
.footer li{list-style:none;font-size:10px;color:#bbb;margin-bottom:4px}
.footer li::before{content:"› ";color:var(--red)}
.newsletter{width:190px}
.newsletter .field{height:20px;background:#333;border:1px solid #555;font-size:9px;color:#999;padding:3px 6px;margin-bottom:6px}
.newsletter .btn{display:inline-block;background:var(--red);color:#fff;font-size:10px;padding:3px 10px}
.col{width:130px}
.social li::before{content:"";display:inline-block;width:10px;height:10px;background:var(--red);margin-right:6px;vertical-align:-1px}
.copyright{position:absolute;left:0;top:1180px;width:878px;height:20px;background:var(--red);color:#fff;font-size:10px;text-align:center;line-height:20px}
</style>
</head>
<body>
<div class="page">
  <header class="header">
    <div class="user-links"><span>New User!</span><span>Register</span><span>Sign in</span><span>Help</span></div>
    <div class="brand"><span class="brand-mark"></span><span class="brand-name">FoxTrail</span></div>
    <nav class="nav"><a class="active">HOME</a><a>COMPANY</a><a>SERVICE</a><a>PRODUCTS</a><a>CONTACTS</a></nav>
  </header>

  <section class="hero" role="img" aria-label="Contact centre agents wearing headsets at their desks">
    <div class="hero-title">Interactive Support</div>
    <div class="hero-sub">Portal for customers</div>
  </section>

  <section class="products">
    <div class="product">
      <span class="product-tab"><svg width="14" height="14"><circle cx="7" cy="7" r="6" fill="#fff"/></svg>LINESIGHT</span>
      <p><svg width="22" height="16"><rect x="1" y="1" width="20" height="12" fill="none" stroke="#fff"/><rect x="8" y="13" width="6" height="3" fill="#fff"/></svg>A software to view call queue by the managers in call centers</p>
    </div>
    <div class="product">
      <span class="product-tab"><svg width="14" height="14"><rect x="2" y="2" width="10" height="10" fill="#fff"/></svg>MASSLOAD</span>
      <p><svg width="22" height="16"><rect x="1" y="3" width="20" height="12" fill="#fff"/></svg>An application to load up list of numbers to be called for the call center guys</p>
    </div>
    <div class="product">
      <span class="product-tab"><svg width="14" height="14"><path d="M7 1 L13 13 L1 13Z" fill="#fff"/></svg>CLUSTRA</span>
      <p><svg width="22" height="16"><circle cx="7" cy="8" r="5" fill="#fff"/><circle cx="15" cy="8" r="5" fill="#bbb"/></svg>software to group up teams and members with the call center agents</p>
    </div>
  </section>

  <main class="main">
    <div class="content">
      <h2>Welcome Dear Visitor!</h2>
      <p class="intro"><span class="lead">A few words about our team, our products and the way we help contact centres run better.</span>
      FoxTrail builds software and delivers professional services for enterprise contact centres across the US and UK. Our tools help managers and administrators watch calls in queue, load large groups of extensions and organise agents into clear, layered groups. Every product is designed to work with Vortiva platforms, so teams can get started quickly and keep their operations running smoothly. From first setup to daily support, our engineers stay close to each customer and answer questions through the interactive support portal and forum.</p>

      <h2>The Best Connection for your better communication</h2>
      <div class="feature">
        <div class="feature-photo" role="img" aria-label="Headset resting on a desk"></div>
        <div>
          <h3>Remote access</h3>
          <span class="tag">Contrary to popular belief</span>
          <p>Reach your contact centre tools from anywhere with secure remote access for every manager.</p>
          <span class="more"><i></i>Read more</span>
        </div>
      </div>
      <div class="feature">
        <div class="feature-photo" role="img" aria-label="Support team at work in an office"></div>
        <div>
          <h3>Member centre</h3>
          <span class="tag">Contrary to popular belief</span>
          <p>Members get product downloads, licence details, forum access and direct help from our team.</p>
          <span class="more"><i></i>Read more</span>
        </div>
      </div>
    </div>

    <aside class="sidebar">
      <div class="services">
        <h4>Our Services</h4>
        <ul>
          <li>Telemarketing Services</li>
          <li>Lead Capture Services</li>
          <li>Advertising Campaign</li>
          <li>Sales Lead Conversion</li>
          <li>Web Enabled Call Centre</li>
          <li>Monitoring systems</li>
          <li>Detection Systems</li>
          <li>Tariffs and Charges</li>
          <li>Client Statistics</li>
        </ul>
      </div>
      <div class="stats">
        <h4>Client Statistics</h4>
        <span class="arrow left"></span><span class="arrow right"></span>
        <blockquote>“Our queue times dropped within weeks and our managers finally see every call as it happens.”</blockquote>
        <cite>— Mara Ellison (New York)</cite>
      </div>
    </aside>
  </main>

  <footer class="footer">
    <div class="newsletter">
      <h5>Newsletter</h5>
      <div class="field">Your e-Mail ID here</div>
      <span class="btn">Subscribe</span>
    </div>
    <div class="col"><h5>Advice</h5><ul><li>FAQs</li><li>Solutions</li><li>Contact</li></ul></div>
    <div class="col"><h5>Join Us</h5><ul><li>Forum</li><li>Careers</li><li>Partners</li></ul></div>
    <div class="col"><h5>Support</h5><ul><li>FAQs</li><li>Your Portal</li><li>Solutions</li></ul></div>
    <div class="col social"><h5>Connect Us</h5><ul><li>Friendwall</li><li>Chirper</li><li>ClipTube</li></ul></div>
  </footer>
  <div class="copyright">© FoxTrail. All rights reserved.</div>
</div>
</body>
</html>
```